900mm double sided Card Ponytail Insert for hair

I need print ready file designs for card packaging inserts for my line of ponytails, These are two sided colour and fold at each end or contain the hair, for structure and so the brand is on display. These will be marketed as luxury ponytails, so we want a simple, soft but luxurious design feel. All the details are below but it will be the logo, photos and simple messaging

Target Market(s)

18-30 females

Industry/Entity Type

Beauty

Font styles to use
Serif

Requirements
Must have
• - Lumera Logo on the back and top front fold.
'Luxury Synthetic Ponytails' Head line
'For effortlessly long and luxurious hair' tag line
'For tutorials, questions and inspiration head to our 'Brightroom' on lumerabeauty.com'
www.lumerabeauty.com
Tag us on socials! @lumerabeautyofficial (pictavo and Chatterloop logos)
3 step-by-step pictures (holding pictures please until i have some taken)
Nice to have
• (notes to designers) view our website to see our branding lumerabeauty.com - it would be good to use our brand colours and somekind of tropical leaves maybe? i'm thinking palm leaves?
- my brand font is Sweet Getaway - but this may only be good for the biggest headings

```html
<!DOCTYPE html>
<html lang="en">
<head>
<meta charset="utf-8">
<title>Lumera Ponytail Insert</title>
<link rel="stylesheet" href="https://fonts.googleapis.com/css2?family=Montserrat:wght@400;600;700&family=Mrs+Saint+Delafield&display=swap">
<style>
  :root {
    --bg: #d3d3d3;
    --card: #ffffff;
    --gold: #c48a3f;
    --mint: #5fc4a5;
    --mint-soft: #bfe6d8;
    --pink: #e8468a;
    --label: #333333;
    --ink: #222222;
    --fold: #9aa0a8;
  }
  * { box-sizing: border-box; }
  html, body {
    margin: 0;
    width: 1200px;
    height: 1030px;
    overflow: hidden;
    background: var(--bg);
    font-family: "Montserrat", Arial, sans-serif;
  }
  .sheet { position: relative; width: 1200px; height: 1030px; }
  .panel { position: absolute; background: var(--card); }
  .panel svg { position: absolute; left: 0; top: 0; }
  .panel--front { left: 90px; top: 27px; width: 267px; height: 924px; }
  .panel--folded { left: 479px; top: 192px; width: 253px; height: 690px; }
  .panel--back { left: 836px; top: 29px; width: 267px; height: 922px; }

  .view-label {
    position: absolute;
    font-weight: 700;
    font-size: 20px;
    letter-spacing: 1px;
    color: var(--label);
    transform: translateX(-50%);
  }

  .brand-mark {
    position: absolute;
    left: 0; right: 0;
    text-align: center;
    font-family: "Mrs Saint Delafield", cursive;
    font-size: 40px;
    color: var(--gold);
    line-height: 1;
  }
  .brand-mark--folded { top: 40px; }
  .brand-mark--flap { top: 82px; transform: rotate(180deg); }

  .back-copy {
    position: absolute;
    left: 13px; width: 241px;
    text-align: center;
    color: var(--gold);
  }
  .headline {
    top: 206px;
    font-family: "Mrs Saint Delafield", cursive;
    font-size: 31px;
    color: var(--ink);
    line-height: 1;
    margin: 0;
    font-weight: 400;
  }
  .tagline { top: 251px; font-size: 10.5px; margin: 0; }
  .info { top: 280px; font-size: 10.5px; line-height: 14px; margin: 0; }

  .step {
    position: absolute;
    border: 1.3px solid var(--ink);
    background: var(--card);
  }
  .step span {
    position: absolute;
    left: 6px; top: 3px;
    font-weight: 700;
    font-size: 19px;
    color: var(--gold);
  }
  .step--1 { left: 121px; top: 357px; width: 106px; height: 131px; transform: rotate(3deg); }
  .step--2 { left: 37px; top: 453px; width: 113px; height: 137px; transform: rotate(-5deg); }
  .step--3 { left: 117px; top: 573px; width: 110px; height: 129px; transform: rotate(2deg); }

  .socials {
    position: absolute;
    left: 13px; width: 241px; top: 730px;
    text-align: center;
    color: var(--gold);
    font-size: 10.5px;
    line-height: 15px;
  }
  .socials p { margin: 0; }
  .social-square {
    display: inline-block;
    width: 8px; height: 8px;
    background: var(--gold);
    margin-right: 3px;
    vertical-align: -1px;
  }
</style>
</head>
<body>
<main class="sheet">

  <section class="panel panel--front" aria-label="Front of insert, unfolded">
    <svg width="267" height="924" viewBox="0 0 267 924">
      <defs>
        <linearGradient id="leafToneFront" x1="0" y1="0" x2="1" y2="1">
          <stop offset="0" stop-color="#8fd6be"/>
          <stop offset="0.5" stop-color="#bfe6d8"/>
          <stop offset="1" stop-color="#e998bd"/>
        </linearGradient>
      </defs>
      <path role="img" aria-label="Tropical pattern of mint palm fronds and pink monstera leaves"
            d="M12,70 C80,38 160,8 255,42 L255,880 C180,905 90,850 12,905 Z"
            fill="url(#leafToneFront)" stroke="var(--gold)" stroke-width="1.6"/>
      <rect x="8" y="147" width="251" height="8" fill="none" stroke="var(--fold)" stroke-width="0.8" stroke-dasharray="3 2"/>
      <rect x="8" y="829" width="251" height="8" fill="none" stroke="var(--fold)" stroke-width="0.8" stroke-dasharray="3 2"/>
    </svg>
  </section>

  <section class="panel panel--folded" aria-label="Insert folded">
    <svg width="253" height="690" viewBox="0 0 253 690">
      <defs>
        <linearGradient id="leafToneFolded" x1="0" y1="0" x2="1" y2="1">
          <stop offset="0" stop-color="#8fd6be"/>
          <stop offset="0.5" stop-color="#bfe6d8"/>
          <stop offset="1" stop-color="#e998bd"/>
        </linearGradient>
      </defs>
      <path role="img" aria-label="Tropical pattern of mint palm fronds and pink monstera leaves"
            d="M5,95 C90,72 170,150 248,122 L248,608 C170,650 90,598 5,640 Z"
            fill="url(#leafToneFolded)"/>
      <rect x="5" y="7" width="243" height="676" fill="none" stroke="var(--gold)" stroke-width="1.6"/>
      <path d="M5,95 C90,72 170,150 248,122 M248,608 C170,650 90,598 5,640" fill="none" stroke="var(--gold)" stroke-width="1.6"/>
    </svg>
    <div class="brand-mark brand-mark--folded">Lumera</div>
  </section>

  <section class="panel panel--back" aria-label="Back of insert, unfolded">
    <svg width="267" height="922" viewBox="0 0 267 922">
      <path d="M12,45 C90,20 180,60 255,30 L255,140 L12,140 Z" fill="none" stroke="var(--gold)" stroke-width="1.6"/>
      <rect x="8" y="144" width="251" height="12" fill="none" stroke="var(--fold)" stroke-width="0.8" stroke-dasharray="3 2"/>
      <rect x="13" y="162" width="241" height="655" fill="none" stroke="var(--gold)" stroke-width="1.6"/>
      <rect x="8" y="824" width="251" height="11" fill="none" stroke="var(--fold)" stroke-width="0.8" stroke-dasharray="3 2"/>
      <path d="M12,840 L255,840 L255,880 C180,902 90,862 12,905 Z" fill="none" stroke="var(--gold)" stroke-width="1.6"/>
    </svg>
    <div class="brand-mark brand-mark--flap">Lumera</div>

    <h1 class="back-copy headline">luxury synthetic ponytails</h1>
    <p class="back-copy tagline">For effortlessly long and luxurious hair.</p>
    <p class="back-copy info">For tutorials, questions and inspiration<br>head to our 'Brightroom' on<br>lumerabeauty.com</p>

    <div class="step step--1"><span>1</span></div>
    <div class="step step--2"><span>2</span></div>
    <div class="step step--3"><span>3</span></div>

    <div class="socials">
      <p>Tag us on socials!</p>
      <p><span class="social-square"></span>Chatterloop @lumerabeautyofficial</p>
      <p><span class="social-square"></span>pictavo @lumerabeautyofficial</p>
    </div>
  </section>

  <div class="view-label" style="left:213px; top:972px;">FRONT</div>
  <div class="view-label" style="left:605px; top:968px;">FOLDED</div>
  <div class="view-label" style="left:987px; top:968px;">BACK</div>

</main>
</body>
</html>
```